Sydney law firm, Prestwicks Solicitors, needs a flyer design!

We need a flyer design for our law firm which has been operating in Sydney for over 35 years. We want to send the flyer out to potential clients and also to existing clients to let them know the range of services that we provide. Our corporate colours are white, red and black and we would like these incorporated somewhat. The final design should be clean, modern and professional.

We would like the design to fit a double sided flyer approx. 210mm high x 100mm wide.

Industry/Entity Type

Law Firm

Font styles to use
Serif
Sans Serif

Colors
eb2026
ffffff

Requirements
Must have
• Details needed on the flyer are:
• Prestwicks Solicitors
• 3/82 Carradine Street, Liverpool, NSW 2170
• (02) 9418 3562
• www.prestwickssolicitors-example.com.au
• info@prestwickssolicitors-example.com.au
• Our areas of practice include:
• Property Law
• Conveyancing
• Leases
• Criminal Law
• Family Law
• Litigation and Dispute Resolution
• Company Law
• Wills and Estates
• Powers of Attorney and Guardianship
Should not have
• a picture of scales or a picture of a gavel

```html
<!DOCTYPE html>
<html lang="en">
<head>
<meta charset="utf-8">
<title>Prestwicks Solicitors – Flyer</title>
<link href="https://fonts.googleapis.com/css2?family=Questrial&display=swap" rel="stylesheet">
<style>
  :root {
    --paper: #ffffff;
    --ink: #141414;
    --brand-red: #eb2026;
    --navy-deep: #131d31;
    --navy-mid: #1f3150;
    --navy-light: #3d5a7c;
    --text-light: #f2f4f8;
  }
  * { margin: 0; padding: 0; box-sizing: border-box; }
  html, body {
    width: 1143px;
    height: 1200px;
    overflow: hidden;
    background: var(--paper);
  }
  .flyer {
    position: relative;
    width: 1143px;
    height: 1200px;
    display: flex;
  }
  .side {
    position: relative;
    width: 571.5px;
    height: 1200px;
    background: var(--paper);
  }
  .brand {
    position: absolute;
    top: 170px;
    left: 0;
    width: 100%;
    display: flex;
    justify-content: center;
    align-items: center;
    gap: 16px;
    font-family: "Questrial", "Century Gothic", sans-serif;
    font-weight: 400;
    font-size: 40px;
    line-height: 1;
    color: var(--ink);
    white-space: nowrap;
  }
  .brand-mark {
    width: 22px;
    height: 22px;
    background: var(--brand-red);
    flex: none;
  }
  .backdrop {
    position: absolute;
    top: 320px;
    left: 0;
    width: 100%;
    height: 880px;
    background:
      radial-gradient(circle at 62% 38%, rgba(220,235,255,0.55) 0, rgba(120,150,190,0.25) 9%, transparent 22%),
      radial-gradient(ellipse at 30% 70%, rgba(150,40,50,0.35) 0, transparent 45%),
      linear-gradient(165deg, var(--navy-deep) 0%, var(--navy-mid) 55%, var(--navy-light) 100%);
  }
  .side + .side .backdrop { border-left: 1px solid rgba(0,0,0,0.35); }
  .contact {
    position: absolute;
    top: 398px;
    left: 0;
    width: 100%;
    text-align: center;
    font-family: "Questrial", "Century Gothic", sans-serif;
    font-style: normal;
    font-size: 24px;
    line-height: 36px;
    color: var(--text-light);
  }
  .contact .gap { height: 45px; }
  .services {
    position: absolute;
    top: 340px;
    left: 58px;
    list-style: none;
    font-family: "Questrial", "Century Gothic", sans-serif;
    font-size: 26px;
    color: var(--text-light);
  }
  .services li {
    height: 72.7px;
    line-height: 40px;
    white-space: nowrap;
  }
  .services li::before { content: "- "; }
</style>
</head>
<body>
<main class="flyer">
  <section class="side side-front">
    <div class="brand"><span class="brand-mark"></span><span class="brand-name">Prestwicks Solicitors</span></div>
    <div class="backdrop" role="img" aria-label="Dark blue digital background with glowing rounded squares, red hexagons and a hand pointing upward to touch a lit button"></div>
    <address class="contact">
      <div>Prestwicks Solicitors</div>
      <div>3/82 Carradine Street, Liverpool, NSW 2170</div>
      <div>Tel: (02) 9418 3562</div>
      <div class="gap"></div>
      <div>www.prestwickssolicitors-example.com.au</div>
      <div>info@prestwickssolicitors-example.com.au</div>
    </address>
  </section>
  <section class="side side-back">
    <div class="brand"><span class="brand-mark"></span><span class="brand-name">Prestwicks Solicitors</span></div>
    <div class="backdrop" role="img" aria-label="Dark blue digital background with glowing rounded squares, red hexagons and a hand pointing upward to touch a lit button"></div>
    <ul class="services">
      <li>Property Law</li>
      <li>Conveyancing</li>
      <li>Leases</li>
      <li>Criminal Law</li>
      <li>Litigation and Dispute Resolution</li>
      <li>Family Law</li>
      <li>Powers of Attorney and Guardianship</li>
      <li>Company Law</li>
      <li>Wills and Estates</li>
    </ul>
  </section>
</main>
</body>
</html>
```